I want a business card design. the company is an infrastructure development company.

Target Market(s)

Government
real estate investors
real estate clients

Industry/Entity Type

Business

```html
<!DOCTYPE html>
<html lang="en">
<head>
<meta charset="utf-8">
<title>Arden Civitas – Business Card</title>
<link rel="stylesheet" href="https://fonts.googleapis.com/css2?family=Exo+2:wght@400;500;600&display=swap">
<style>
  :root {
    --page-bg: #e9e9e7;
    --card-white: #f7f7f7;
    --card-blue: #1ea9ea;
    --brand-blue: #2f9fe0;
    --accent-red: #e8383d;
    --ink-dark: #3a3a3a;
    --ink-light: #ffffff;
  }
  * { margin: 0; padding: 0; box-sizing: border-box; }
  html, body {
    width: 1200px;
    height: 1085px;
    overflow: hidden;
    background: var(--page-bg);
    font-family: "Exo 2", sans-serif;
  }
  .canvas {
    width: 1200px;
    height: 1085px;
    display: flex;
    align-items: center;
    justify-content: center;
  }
  .business-card {
    position: relative;
    width: 1000px;
    height: 572px;
    background: var(--card-white);
    box-shadow: 0 10px 30px rgba(0,0,0,0.18);
    overflow: hidden;
  }
  .contact-panel {
    position: absolute;
    inset: 0;
    width: 1000px;
    height: 572px;
  }
  .contact-group {
    position: absolute;
    right: 620px;
    text-align: right;
    color: var(--ink-light);
    font-size: 27px;
    font-weight: 500;
    line-height: 1.3;
    letter-spacing: 0.5px;
    white-space: nowrap;
    transform: translateY(-50%);
  }
  .contact-group.phone { top: 118px; }
  .contact-group.address { top: 278px; }
  .contact-group.web { top: 442px; }
  .brand {
    position: absolute;
    left: 545px;
    top: 120px;
    display: flex;
    align-items: center;
    gap: 18px;
  }
  .brand-mark {
    width: 34px;
    height: 34px;
    background: var(--accent-red);
  }
  .brand-name {
    font-size: 46px;
    font-weight: 600;
    letter-spacing: 2px;
    color: var(--brand-blue);
    text-transform: uppercase;
    white-space: nowrap;
  }
  .person {
    position: absolute;
    left: 600px;
    top: 300px;
  }
  .person-name {
    font-size: 34px;
    font-weight: 500;
    letter-spacing: 2px;
    color: var(--accent-red);
    text-transform: uppercase;
    white-space: nowrap;
  }
  .person-title {
    font-size: 30px;
    font-weight: 500;
    color: var(--ink-dark);
    margin-top: 4px;
  }
</style>
</head>
<body>
<main class="canvas">
  <article class="business-card">
    <svg class="contact-panel" viewBox="0 0 1000 572" aria-hidden="true">
      <path fill="var(--card-blue)" d="
        M0 0 H0 V572 H390
        V502 C390 490 386 486 400 486
        C468 486 468 386 400 386
        C386 386 390 380 390 370
        V338 C390 326 386 322 400 322
        C468 322 468 222 400 222
        C386 222 390 216 390 206
        V176 C390 164 386 160 400 160
        C468 160 468 60 400 60
        C386 60 390 54 390 44
        V0 Z"/>
      <g fill="none" stroke="var(--ink-light)" stroke-width="3">
        <circle cx="420" cy="110" r="26"/>
        <circle cx="420" cy="272" r="26"/>
        <circle cx="420" cy="436" r="26"/>
      </g>
      <path fill="var(--ink-light)" d="M410 98 c3 -2 6 -1 7 2 l3 6 c1 2 0 4 -2 5 l-2 1 c1 4 4 8 8 10 l2 -2 c1 -2 3 -2 5 -1 l6 3 c2 1 3 4 1 6 l-3 3 c-4 3 -11 1 -18 -5 c-7 -6 -11 -14 -10 -19 z"/>
      <path fill="var(--ink-light)" d="M420 256 c-9 0 -15 7 -15 15 c0 10 15 25 15 25 c0 0 15 -15 15 -25 c0 -8 -6 -15 -15 -15 z"/>
      <circle cx="420" cy="271" r="5.5" fill="var(--card-blue)"/>
      <g fill="none" stroke="var(--ink-light)" stroke-width="2.2">
        <circle cx="420" cy="436" r="15"/>
        <ellipse cx="420" cy="436" rx="6.5" ry="15"/>
        <line x1="405" y1="436" x2="435" y2="436"/>
        <path d="M408 427 H432 M408 445 H432"/>
      </g>
    </svg>

    <div class="contact-group phone">
      <p>020 481 3356</p>
      <p>020 481 3357</p>
    </div>
    <div class="contact-group address">
      <p>045 12th floor,</p>
      <p>Harbour Link Road</p>
      <p>NVR</p>
    </div>
    <div class="contact-group web">
      <p>info@ardenciv.com</p>
      <p>ardencivitas.com</p>
    </div>

    <div class="brand">
      <span class="brand-mark"></span>
      <span class="brand-name">Arden Civitas</span>
    </div>

    <div class="person">
      <p class="person-name">Daniel Hartwell</p>
      <p class="person-title">Managing Director</p>
    </div>
  </article>
</main>
</body>
</html>
```